CD Cover Design Project For New Electronic Album

Hi, I need cover artwork for my forth coming electronic music album. The requirement is for the single page front insert and also the tray liner (rear inlay). You can find the required specifications here http://www.quillpressmedia.co.uk/artwork_specs.php

The title of the album is Velmorandine and the artists name is Owen Pritcham.

The theme of the album is the world and water, so that needs to play a big part in the imagery. An example of the kind of thing I'm looking for can be found at

http://www.brackenimagery.com/media/482736/view (this image is copyrighted, so please don't use for your own work).

I have no preference for the rear inlay, so please feel free to come up with something, so long as it is in keeping with the design for the front. There needs to be room for the song titles though, but not sure how many yet!

Good luck!
Updates

If you would like to hear a small section of the type of music to be on the album, you can listen at my tunewharf account.

https://tunewharf.com/copper-lantern/sets/velmorandine

This also contains a mock up of an album cover that was originally thought of, however permission could not be gained for the use of the image.

Industry/Entity Type

Electronic

```html
<!DOCTYPE html>
<html lang="en">
<head>
<meta charset="utf-8">
<title>Velmorandine – Owen Pritcham – CD Artwork</title>
<link rel="stylesheet" href="https://fonts.googleapis.com/css2?family=Quicksand:wght@300;400&display=swap">
<style>
  :root {
    --sheet-top: #ffffff;
    --sheet-bottom: #d6d6d6;
    --label-ink: #4a2a36;
    --cover-deep: #2a1719;
    --cover-mid: #3d2228;
    --cover-haze: #5b3d56;
    --inlay-top: #522036;
    --inlay-bottom: #231118;
    --planet-ocean: #2f4a78;
    --planet-cloud: #e9ecef;
    --planet-land: #b79f7e;
    --title-ink: #ffffff;
    --artist-ink: #e6d6dc;
    --disc-face: #ffffff;
    --track-ink: #6e3d58;
    --spine-ink: #b79aa8;
  }

  * { margin: 0; padding: 0; box-sizing: border-box; }

  html, body {
    width: 1200px;
    height: 708px;
    overflow: hidden;
  }

  body {
    position: relative;
    background: linear-gradient(to bottom, var(--sheet-top) 0%, var(--sheet-top) 18%, var(--sheet-bottom) 100%);
    font-family: "Quicksand", sans-serif;
  }

  .panel-label {
    position: absolute;
    top: 74px;
    font-weight: 300;
    font-size: 48px;
    line-height: 1;
    color: var(--label-ink);
    letter-spacing: 0.5px;
  }
  .panel-label--front { left: 90px; }
  .panel-label--rear { left: 601px; }

  /* Front insert */
  .front-cover {
    position: absolute;
    left: 92px;
    top: 140px;
    width: 413px;
    height: 408px;
    overflow: hidden;
    box-shadow: 0 1px 3px rgba(0,0,0,0.25);
  }

  .front-cover__backdrop {
    position: absolute;
    inset: 0;
    background:
      radial-gradient(ellipse 70% 30% at 60% 100%, var(--cover-haze) 0%, transparent 100%),
      radial-gradient(ellipse 60% 40% at 20% 10%, #4a3040 0%, transparent 100%),
      linear-gradient(160deg, var(--cover-mid) 0%, var(--cover-deep) 100%);
  }

  .front-cover__planet {
    position: absolute;
    left: 106px;
    top: 60px;
    width: 254px;
    height: 254px;
    border-radius: 50%;
    background:
      radial-gradient(circle at 55% 25%, var(--planet-land) 0%, transparent 30%),
      radial-gradient(circle at 40% 65%, var(--planet-cloud) 0%, transparent 35%),
      radial-gradient(circle at 38% 35%, #7f93b0 0%, var(--planet-ocean) 60%, #1b2a46 100%);
    box-shadow: 0 0 18px rgba(120,140,190,0.25);
  }

  .front-cover__title {
    position: absolute;
    right: 34px;
    top: 322px;
    font-weight: 300;
    font-size: 47px;
    line-height: 1;
    color: var(--title-ink);
    letter-spacing: 0.5px;
  }

  .front-cover__artist {
    position: absolute;
    right: 36px;
    top: 374px;
    font-weight: 300;
    font-size: 18px;
    line-height: 1;
    color: var(--artist-ink);
  }

  /* Rear inlay */
  .rear-inlay {
    position: absolute;
    left: 601px;
    top: 141px;
    width: 517px;
    height: 408px;
    overflow: hidden;
    background: linear-gradient(to bottom, var(--inlay-top) 0%, var(--inlay-bottom) 100%);
    box-shadow: 0 1px 3px rgba(0,0,0,0.25);
  }

  .rear-inlay__disc {
    position: absolute;
    left: 126px;
    top: 62px;
    width: 278px;
    height: 278px;
    border-radius: 50%;
    background: var(--disc-face);
    display: flex;
    align-items: center;
    justify-content: center;
  }

  .track-list {
    list-style: none;
    text-align: center;
    font-weight: 300;
    font-size: 15.5px;
    line-height: 20px;
    color: var(--track-ink);
    margin-top: -26px;
  }

  .spine {
    position: absolute;
    top: 50%;
    white-space: nowrap;
    font-weight: 300;
    font-size: 12px;
    letter-spacing: 0.4px;
    color: var(--spine-ink);
    word-spacing: 2px;
  }
  .spine__divider { margin: 0 12px; }

  .spine--left {
    left: 21px;
    transform: translate(-50%, -50%) rotate(-90deg);
  }
  .spine--right {
    left: 496px;
    transform: translate(-50%, -50%) rotate(90deg);
  }
</style>
</head>
<body>

  <h2 class="panel-label panel-label--front">Front</h2>
  <h2 class="panel-label panel-label--rear">Rear Inlay</h2>

  <section class="front-cover">
    <div class="front-cover__backdrop" role="img" aria-label="Night sky with faint stars and purple nebula haze"></div>
    <div class="front-cover__planet" role="img" aria-label="Photograph of the Earth seen from space with a water droplet over the continent"></div>
    <h1 class="front-cover__title">Velmorandine</h1>
    <p class="front-cover__artist">Owen Pritcham</p>
  </section>

  <section class="rear-inlay" role="img" aria-label="Dark plum starry sky background">
    <div class="spine spine--left">Owen Pritcham<span class="spine__divider">|</span>Velmorandine</div>

    <div class="rear-inlay__disc">
      <ol class="track-list">
        <li>1. First Song</li>
        <li>2. Second Song</li>
        <li>3. Third Song</li>
        <li>4. Fourth Song</li>
        <li>5. Fifth Song</li>
        <li>6. Sixth Song</li>
        <li>7. Seventh song</li>
      </ol>
    </div>

    <div class="spine spine--right">Owen Pritcham<span class="spine__divider">|</span>Velmorandine</div>
  </section>

</body>
</html>
```